Outward Compass Podcast Graphic

I need a graphic button to support my new podcast. It must meet the requirements for Tunevault. Below is my business log but I am not sure I want to use this or have something different. The topic of my podcast is building resilience. I want something clean and simple that stands out. I want it to be bright and modern.

Target Market(s)

People who want to increase their resilience.

Industry/Entity Type

Business

Font styles to use
Decorative

Colors
00a990
f37122

Requirements
Must have
• Must meet the criteria for Tunevault.

```html
<!DOCTYPE html>
<html lang="en">
<head>
<meta charset="utf-8">
<title>Building Resilience – Outward Compass Podcast</title>
<link href="https://fonts.googleapis.com/css2?family=Montserrat:wght@700;800&display=swap" rel="stylesheet">
<style>
  :root {
    --paper: #ffffff;
    --teal-deep: #27aa9f;
    --teal-light: #55c4a6;
    --coral: #e3867f;
    --coral-light: #ea968d;
    --bar-black: #0b0b0b;
    --photo-light: #d9d9d9;
    --photo-mid: #8a8a8a;
    --brand-orange: #f37122;
  }
  html, body {
    margin: 0;
    padding: 0;
    width: 1200px;
    height: 1200px;
    overflow: hidden;
    background: var(--paper);
  }
  .cover {
    position: relative;
    width: 1200px;
    height: 1200px;
    background: var(--paper);
    font-family: "Montserrat", "Helvetica Neue", Arial, sans-serif;
  }
  .cover__art {
    position: absolute;
    inset: 0;
    width: 1200px;
    height: 1200px;
  }
  .title {
    font-family: "Montserrat", "Helvetica Neue", Arial, sans-serif;
    font-weight: 800;
  }
  .brand {
    position: absolute;
    right: 72px;
    top: 1086px;
    margin: 0;
    text-align: right;
    font-family: "Montserrat", "Helvetica Neue", Arial, sans-serif;
    font-weight: 800;
    font-size: 28px;
    line-height: 30px;
    letter-spacing: -0.5px;
    color: var(--brand-orange);
  }
</style>
</head>
<body>
<main class="cover">
  <svg class="cover__art" viewBox="0 0 1200 1200" xmlns="http://www.w3.org/2000/svg">
    <defs>
      <linearGradient id="teal-fill" x1="0" y1="0" x2="1" y2="0">
        <stop offset="0" stop-color="var(--teal-deep)"/>
        <stop offset="0.45" stop-color="var(--teal-deep)"/>
        <stop offset="1" stop-color="var(--teal-light)"/>
      </linearGradient>
      <linearGradient id="coral-fill" x1="0" y1="0" x2="1" y2="0">
        <stop offset="0" stop-color="var(--coral)"/>
        <stop offset="1" stop-color="var(--coral-light)"/>
      </linearGradient>
      <radialGradient id="scene-fill" cx="0.5" cy="0.35" r="0.6">
        <stop offset="0" stop-color="var(--photo-light)"/>
        <stop offset="0.6" stop-color="var(--photo-mid)"/>
        <stop offset="1" stop-color="var(--bar-black)"/>
      </radialGradient>
      <clipPath id="bar-windows">
        <rect x="266" y="560" width="91" height="488"/>
        <rect x="421" y="560" width="97" height="488"/>
        <rect x="581" y="560" width="124" height="488"/>
        <rect x="768" y="560" width="97" height="488"/>
        <rect x="928" y="560" width="71" height="488"/>
      </clipPath>
    </defs>

    <text class="title title--top" x="1130" y="336" text-anchor="end"
          font-size="150" textLength="684" lengthAdjust="spacingAndGlyphs"
          fill="url(#teal-fill)">BUILDING</text>
    <text class="title title--main" x="97" y="478"
          font-size="196" textLength="1033" lengthAdjust="spacingAndGlyphs"
          fill="url(#coral-fill)">RESILIENCE</text>

    <g class="bars" clip-path="url(#bar-windows)">
      <rect x="260" y="560" width="745" height="488" fill="var(--bar-black)"/>
      <rect class="bars__scene" x="421" y="668" width="372" height="326"
            fill="url(#scene-fill)" role="img"
            aria-label="Black and white photo of a young woman under a white umbrella reading a book in the rain, seen through the bars"/>
    </g>
  </svg>

  <p class="brand">Outward<br>Compass</p>
</main>
</body>
</html>
```